Velmoro Cabinets Letter Head and Email Signature

Hi
I would love a design package for a letterhead, email signature, even update my business card if you like if you can come up with a great idea for my new high end cabinet shop. Velmoro Cabinets brings timeless craftsmanship to modern interiors, specializing in high end, custom cabinetry designed for architects and interior designers.

Target Market(s)

high end, luxury market

Industry/Entity Type

cabinet making

Requirements
Must have
• my colours of logo as the theme

```html
<!DOCTYPE html>
<html lang="en">
<head>
<meta charset="utf-8">
<title>Velmoro Cabinets — Stationery Suite</title>
<link href="https://fonts.googleapis.com/css2?family=Montserrat:wght@400;500;600&display=swap" rel="stylesheet">
<style>
  :root {
    --green: #4e7d4f;
    --black: #0a0b0c;
    --white: #ffffff;
    --ink: #1d1d1d;
    --board: #6b3a1e;
    --rule: #e3e6e3;
  }
  * { box-sizing: border-box; margin: 0; padding: 0; }
  html, body { width: 1051px; height: 1200px; overflow: hidden; }
  body {
    background: var(--board);
    font-family: "Montserrat", sans-serif;
    color: var(--ink);
    position: relative;
  }
  .section-label { position: absolute; color: var(--white); font-size: 12.5px; font-weight: 500; }
  .piece { position: absolute; background: var(--white); overflow: hidden; }
  .abs { position: absolute; }

  /* brand name block */
  .brand { display: flex; align-items: center; gap: 6px; font-weight: 500; color: var(--green); white-space: nowrap; }
  .brand .mark { border: 1.5px solid currentColor; display: inline-block; flex: none; }
  .brand.on-green { color: var(--white); }

  .contact { display: flex; align-items: center; gap: 5px; white-space: nowrap; }
  .contact svg { flex: none; }
  .name { color: var(--green); font-weight: 600; }
  .role { font-size: 5px; color: var(--ink); }
  .tagline-green { color: var(--green); }

  /* letterhead */
  .letterhead { left: 92px; top: 70px; width: 560px; height: 725px; }
  .letterhead .brand { left: 20px; top: 24px; font-size: 22px; }
  .letterhead .brand .mark { width: 22px; height: 22px; }
  .letterhead .tagline { right: 14px; top: 20px; text-align: right; font-size: 10.5px; font-weight: 600; line-height: 1.5; }
  .letterhead .tag-bar { right: 0; top: 21px; width: 2px; height: 29px; background: var(--green); }
  .letterhead .head-rule-green { left: 0; top: 70px; width: 396px; height: 1.5px; background: var(--green); }
  .letterhead .head-rule-dark { left: 401px; top: 70px; width: 159px; height: 1.5px; background: var(--ink); }
  .letterhead .foot-rule { left: 0; top: 680px; width: 351px; height: 1.5px; background: var(--green); }
  .letterhead .contact { top: 695px; font-size: 10.5px; }

  /* business cards */
  .card { left: 707px; width: 230px; height: 131px; }
  .card.dark { background: var(--black); }
  .card.green { background: var(--green); }
  .card .center { position: absolute; left: 0; right: 0; display: flex; flex-direction: column; align-items: center; }
  .card .brand { font-size: 19px; }
  .card .brand .mark { width: 18px; height: 18px; }
  .card .slogan { color: var(--white); font-size: 8px; margin-top: 16px; }
  .card .band { position: absolute; left: 0; bottom: 0; width: 100%; height: 25px; background: var(--green); color: var(--white); font-size: 8px; display: flex; align-items: center; justify-content: center; }
  .card-front .name { font-size: 9px; }
  .card-front .contact { font-size: 6.5px; }
  .card-front .mark-box { right: 14px; top: 60px; width: 46px; height: 46px; border: 2px solid var(--ink); }

  /* email signatures */
  .sig .contact { font-size: 7px; }
  .sig-1 { left: 101px; top: 830px; width: 372px; height: 131px; }
  .sig-1 .side { left: 0; top: 0; width: 143px; height: 100%; background: var(--black); }
  .sig-1 .band { left: 143px; bottom: 0; right: 0; height: 24px; background: var(--green); color: var(--white); font-size: 7.5px; font-weight: 600; padding-left: 17px; display: flex; align-items: center; }
  .sig-2, .sig-4 { left: 489px; width: 493px; }
  .sig-2 { top: 824px; height: 138px; }
  .sig-4 { top: 1000px; height: 149px; }
  .sig-2 .brand, .sig-4 .brand { left: 16px; top: 38px; font-size: 14px; }
  .sig-2 .brand .mark, .sig-4 .brand .mark { width: 15px; height: 15px; }
  .divider-v { width: 1px; background: var(--rule); }
  .divider-h { height: 1px; background: var(--rule); }
  .info-row { left: 203px; width: 276px; display: flex; justify-content: space-between; align-items: center; }
  .info-row .contact { font-size: 6.5px; gap: 4px; }
  .social { display: flex; align-items: center; gap: 4px; font-size: 8px; font-weight: 500; white-space: nowrap; }
  .social i { width: 12px; height: 12px; border: 1px solid #888; border-radius: 50%; display: inline-block; }
  .sig-3 { left: 104px; top: 1000px; width: 372px; height: 149px; }
  .sig-3 .band { left: 0; bottom: 0; width: 336px; height: 25px; background: var(--black); color: var(--white); font-size: 6.5px; letter-spacing: 1px; padding-left: 11px; display: flex; align-items: center; }
  .sig-3 .chip, .sig-4 .chip { width: 11px; height: 11px; border: 1px solid rgba(255,255,255,.8); }
  .sig-3 .chip-box { right: 0; bottom: 0; width: 36px; height: 25px; background: var(--green); display: flex; align-items: center; justify-content: center; }
  .sig-4 .band { left: 0; bottom: 0; width: 100%; height: 25px; background: var(--green); color: var(--white); font-size: 8px; padding: 0 16px; display: flex; align-items: center; justify-content: space-between; }
</style>
</head>
<body>

<svg width="0" height="0" style="position:absolute">
  <defs>
    <symbol id="icon-phone" viewBox="0 0 16 16"><circle cx="8" cy="8" r="7" fill="none" stroke="currentColor" stroke-width="1.2"/><path d="M6 4.5 l1.3 1.8 -0.8 1 c0.5 1.2 1.2 1.9 2.2 2.4 l1-0.8 1.8 1.3 -0.8 1.2 c-2.8-0.3-5.4-3-5.7-5.7z" fill="currentColor"/></symbol>
    <symbol id="icon-mail" viewBox="0 0 16 16"><path d="M1 6 L8 2 L15 6 V14 H1 Z" fill="currentColor"/><path d="M1 6 L8 10 L15 6" fill="none" stroke="#fff" stroke-width="1.2"/></symbol>
    <symbol id="icon-dot" viewBox="0 0 16 16"><circle cx="8" cy="8" r="6.5" fill="none" stroke="currentColor" stroke-width="1.5"/></symbol>
  </defs>
</svg>

<!-- Letterhead -->
<div class="section-label" style="left:92px;top:41px;">Letterhead</div>
<div class="piece letterhead">
  <div class="abs brand"><span class="mark"></span>Velmoro Cabinets</div>
  <div class="abs tagline">REFINED CRAFTMANSHIP,<br>LUXURY BEAUTY</div>
  <div class="abs tag-bar"></div>
  <div class="abs head-rule-green"></div>
  <div class="abs head-rule-dark"></div>
  <div class="abs foot-rule"></div>
  <div class="abs contact" style="left:19px;"><svg width="16" height="16" style="color:var(--green)"><use href="#icon-phone"/></svg>0400 128 456</div>
  <div class="abs contact" style="left:151px;"><svg width="16" height="16" style="color:var(--green)"><use href="#icon-mail"/></svg>info@velmorocabinets.com.au</div>
  <div class="abs contact" style="left:388px;"><svg width="16" height="16"><use href="#icon-dot"/></svg>@velmoro.cabinets</div>
</div>

<!-- Business cards -->
<div class="section-label" style="left:844px;top:70px;">Business Cards</div>

<div class="piece card card-front" style="top:94px;">
  <div class="abs name" style="left:12px;top:14px;">Marcus Delane</div>
  <div class="abs role" style="left:12px;top:28px;">Director Craftsman</div>
  <div class="abs contact" style="left:12px;top:49px;"><svg width="9" height="9" style="color:var(--green)"><use href="#icon-phone"/></svg>0400 128 456</div>
  <div class="abs contact" style="left:12px;top:63px;"><svg width="9" height="9" style="color:var(--green)"><use href="#icon-mail"/></svg>info@velmorocabinets.com.au</div>
  <div class="abs contact" style="left:12px;top:78px;"><svg width="9" height="9" style="color:var(--green)"><use href="#icon-dot"/></svg>@velmoro.cabinets</div>
  <div class="abs tagline-green" style="left:12px;top:106px;font-size:6px;">Refined Craftmanship, Luxury Beauty</div>
  <div class="abs mark-box"></div>
</div>

<div class="piece card dark" style="top:240px;">
  <div class="center" style="top:52px;"><div class="brand"><span class="mark"></span>Velmoro Cabinets</div></div>
</div>

<div class="piece card dark" style="top:380px;">
  <div class="center" style="top:40px;"><div class="brand"><span class="mark"></span>Velmoro Cabinets</div><div class="slogan">Refined Craftmanship, Luxury Beauty</div></div>
</div>

<div class="piece card green" style="top:529px;">
  <div class="center" style="top:40px;"><div class="brand on-green"><span class="mark"></span>Velmoro Cabinets</div><div class="slogan">Refined Craftmanship, Luxury Beauty</div></div>
</div>

<div class="piece card dark" style="top:669px;">
  <div class="center" style="top:40px;"><div class="brand"><span class="mark"></span>Velmoro Cabinets</div></div>
  <div class="band">Refined Craftmanship, Luxury Beauty</div>
</div>

<!-- Email signature 1 -->
<div class="piece sig sig-1">
  <div class="abs side"></div>
  <div class="abs brand" style="left:11px;top:23px;font-size:10.5px;gap:5px;"><span class="mark" style="width:11px;height:11px;"></span>Velmoro Cabinets</div>
  <div class="abs name" style="left:160px;top:15px;font-size:9px;">Marcus Delane</div>
  <div class="abs role" style="left:160px;top:29px;">Director Craftsman</div>
  <div class="abs contact" style="left:160px;top:49px;"><svg width="9" height="9" style="color:var(--green)"><use href="#icon-phone"/></svg>0400 128 456</div>
  <div class="abs contact" style="left:160px;top:63px;"><svg width="9" height="9" style="color:var(--green)"><use href="#icon-mail"/></svg>info@velmorocabinets.com.au</div>
  <div class="abs contact" style="left:160px;top:78px;"><svg width="9" height="9" style="color:var(--green)"><use href="#icon-dot"/></svg>@velmoro.cabinets</div>
  <div class="abs" style="left:300px;top:20px;width:58px;height:58px;border:2.5px solid var(--ink);"></div>
  <div class="abs band">Refined Craftmanship, Luxury Beauty</div>
</div>
<div class="section-label" style="left:104px;top:966px;">Email Signature - Option 1</div>

<!-- Email signature 2 -->
<div class="piece sig sig-2">
  <div class="abs brand"><span class="mark"></span>Velmoro Cabinets</div>
  <div class="abs" style="left:16px;top:105px;font-size:8.5px;">Refined Craftmanship, Luxury Beauty</div>
  <div class="abs divider-v" style="left:187px;top:25px;height:90px;"></div>
  <div class="abs name" style="left:203px;top:25px;font-size:12px;">Marcus Delane</div>
  <div class="abs" style="left:203px;top:42px;font-size:7px;font-weight:500;">Director Craftsman</div>
  <div class="abs divider-h" style="left:203px;top:60px;width:276px;"></div>
  <div class="abs info-row" style="top:70px;">
    <div class="contact"><svg width="10" height="10"><use href="#icon-phone"/></svg>0400 128 456</div>
    <div class="contact"><svg width="10" height="10"><use href="#icon-mail"/></svg>info@velmorocabinets.com.au</div>
    <div class="contact"><svg width="10" height="10"><use href="#icon-dot"/></svg>@velmoro.cabinets</div>
  </div>
  <div class="abs divider-h" style="left:203px;top:88px;width:276px;"></div>
  <div class="abs info-row" style="top:99px;">
    <div class="social"><i></i>Searchly</div>
    <div class="social"><i></i>ProLink</div>
    <div class="social"><i></i>Friendbook</div>
    <div class="social"><i></i>Snapgram</div>
  </div>
</div>
<div class="section-label" style="left:496px;top:966px;">Email Signature - Option 2</div>

<!-- Email signature 3 -->
<div class="piece sig sig-3">
  <div class="abs brand" style="left:11px;top:13px;font-size:13px;"><span class="mark" style="width:13px;height:13px;"></span>Velmoro Cabinets</div>
  <div class="abs" style="left:11px;top:86px;white-space:nowrap;"><span class="name" style="font-size:9px;">Marcus Delane,</span> <span style="font-size:6px;">Director Craftsman</span></div>
  <div class="abs contact" style="left:11px;top:105px;"><svg width="11" height="11" style="color:var(--green)"><use href="#icon-phone"/></svg>0400 128 456</div>
  <div class="abs contact" style="left:100px;top:105px;"><svg width="11" height="11" style="color:var(--green)"><use href="#icon-mail"/></svg>info@velmorocabinets.com.au</div>
  <div class="abs contact" style="left:236px;top:105px;"><svg width="11" height="11" style="color:var(--green)"><use href="#icon-dot"/></svg>@velmoro.cabinets</div>
  <div class="abs band">REFINED CRAFTMANSHIP, LUXURY BEAUTY</div>
  <div class="abs chip-box"><span class="chip"></span></div>
</div>
<div class="section-label" style="left:109px;top:1154px;">Email Signature - Option 3</div>

<!-- Email signature 4 -->
<div class="piece sig sig-4">
  <div class="abs brand"><span class="mark"></span>Velmoro Cabinets</div>
  <div class="abs divider-v" style="left:187px;top:25px;height:90px;"></div>
  <div class="abs name" style="left:203px;top:25px;font-size:12px;">Marcus Delane</div>
  <div class="abs" style="left:203px;top:42px;font-size:7px;font-weight:500;">Director Craftsman</div>
  <div class="abs divider-h" style="left:203px;top:55px;width:276px;"></div>
  <div class="abs info-row" style="top:64px;">
    <div class="contact"><svg width="10" height="10"><use href="#icon-phone"/></svg>0400 128 456</div>
    <div class="contact"><svg width="10" height="10"><use href="#icon-mail"/></svg>info@velmorocabinets.com.au</div>
    <div class="contact"><svg width="10" height="10"><use href="#icon-dot"/></svg>@velmoro.cabinets</div>
  </div>
  <div class="abs divider-h" style="left:203px;top:82px;width:276px;"></div>
  <div class="abs info-row" style="top:93px;">
    <div class="social"><i></i>Searchly</div>
    <div class="social"><i></i>ProLink</div>
    <div class="social"><i></i>Friendbook</div>
    <div class="social"><i></i>Snapgram</div>
  </div>
  <div class="abs band"><span>Refined Craftmanship, Luxury Beauty</span><span class="chip"></span></div>
</div>
<div class="section-label" style="left:496px;top:1154px;">Email Signature - Option 4</div>

</body>
</html>
```